5x8" package design for beauty / skin care product in a mylar bag

Brevona Works’ Glycolic Acid Powder is pure glycolic acid powder that, when mixed with water, creates glycolic acid solution. Depending on the amount of water added to the powder, you can create different strengths of the solution. Commerical products use between 10 and 70% glycolic acid solution in products. Brevona Works is part of the Calmora hair care company. One of our products use glycolic acid and we can repurpose the raw ingredient alone for retail sales targeting do-it-yourself at home beauty and skin care makers.

Most sellers of glycolic acid powder use basic packaging. Brevona Works intends to create professional, standout packaging that reinforces the quality of the glycolic acid powder we are selling and is consistent with other Calmora brand products sold.

Package design is for a 5x8" matte finished, top loading, resealable pouch. Just looking for front design initially. Second project will include back pouch design using format or design from the front of package.

```html
<!DOCTYPE html>
<html lang="en">
<head>
<meta charset="utf-8">
<title>Brevona Works Glycolic Acid Powder – Pouch Front</title>
<link href="https://fonts.googleapis.com/css2?family=Archivo+Black&family=Oswald:wght@500;600&family=Questrial&display=swap" rel="stylesheet">
<style>
  :root {
    --backdrop: #e8e7e9;
    --orchid: #a8658f;
    --orchid-light: #b87aa0;
    --olive: #8b854b;
    --teal: #2f8c92;
    --teal-deep: #1a6870;
    --ink: #1f1f1f;
    --white: #ffffff;
    --powder: #e4e2de;
  }
  * { box-sizing: border-box; margin: 0; padding: 0; }
  html, body { width: 1200px; height: 982px; overflow: hidden; }
  body { background: var(--backdrop); position: relative; font-family: "Questrial", sans-serif; }

  .pouch {
    position: absolute; left: 374px; top: 170px; width: 453px; height: 641px;
    border-radius: 14px 14px 0 0; overflow: hidden;
    background: linear-gradient(180deg, var(--orchid-light) 0%, var(--orchid) 40%);
  }
  .pouch__seal-label {
    position: absolute; top: 44px; width: 100%; text-align: center;
    font-family: "Oswald", sans-serif; font-weight: 600; font-size: 13px; color: var(--white);
  }
  .pouch__zipper { position: absolute; left: 22px; right: 22px; top: 70px; height: 26px; }

  .brand { position: absolute; top: 128px; left: 0; width: 100%; text-align: center; }
  .brand__name { font-size: 40px; color: var(--white); letter-spacing: 3px; line-height: 1.1; }
  .brand__descriptor {
    margin-top: 6px; font-size: 10px; color: var(--white); opacity: .75; letter-spacing: 1px;
  }
  .brand__formula {
    display: inline-block; margin-left: 6px; padding: 0 5px; border: 1px solid var(--white);
    font-size: 9px;
  }

  .product-title {
    position: absolute; top: 240px; width: 100%; text-align: center;
    font-size: 42px; color: var(--white);
  }
  .format-band {
    position: absolute; top: 292px; left: 0; width: 100%; height: 62px; background: var(--olive);
    display: flex; align-items: center; justify-content: center;
  }
  .format-band__label { font-family: "Archivo Black", sans-serif; font-size: 48px; color: var(--white); letter-spacing: 1px; }

  .lower-panel {
    position: absolute; top: 354px; left: 0; width: 100%; bottom: 0;
    background: radial-gradient(ellipse at 30% 25%, #4a9da6 0%, var(--teal) 35%, var(--teal-deep) 100%);
  }
  .uses {
    position: absolute; top: 20px; left: 56px; right: 56px; display: flex; justify-content: space-between;
    font-family: "Oswald", sans-serif; font-weight: 500; font-size: 17px; color: var(--white);
    border-bottom: 1px solid rgba(255,255,255,.25); padding-bottom: 3px;
  }
  .uses__sep { opacity: .5; }

  .free-from {
    position: absolute; top: 66px; left: 44px; width: 68px; height: 86px; background: var(--orchid);
    text-align: center; color: var(--white); font-family: "Oswald", sans-serif; font-weight: 500;
    font-size: 10px; line-height: 1.25; padding: 3px;
  }
  .free-from__value {
    background: var(--olive); font-family: "Archivo Black", sans-serif; font-size: 24px;
    line-height: 38px; margin-bottom: 3px;
  }

  .powder-visual {
    position: absolute; left: 48px; top: 70px; width: 368px; height: 214px;
    background: radial-gradient(ellipse 55% 75% at 55% 70%, var(--powder) 0%, rgba(228,226,222,.85) 55%, rgba(228,226,222,0) 100%);
  }
  .net-weight {
    position: absolute; bottom: 8px; width: 100%; text-align: center;
    font-family: "Oswald", sans-serif; font-weight: 600; font-size: 17px; color: var(--ink);
  }
</style>
</head>
<body>
  <main class="pouch">
    <p class="pouch__seal-label">RESEABLE POUCH</p>
    <svg class="pouch__zipper" viewBox="0 0 409 26" preserveAspectRatio="none" aria-hidden="true">
      <line x1="0" y1="6" x2="409" y2="6" stroke="#c795b3" stroke-width="3"/>
      <line x1="0" y1="20" x2="409" y2="20" stroke="#9a5a82" stroke-width="3"/>
    </svg>

    <div class="brand">
      <p class="brand__name">Brevona Works</p>
      <p class="brand__descriptor">GLYCOLIC ACID POWDER <span class="brand__formula">C₂H₄O₃</span></p>
    </div>

    <h1 class="product-title">Glycolic Acid</h1>
    <div class="format-band"><span class="format-band__label">POWDER</span></div>

    <section class="lower-panel">
      <p class="uses">
        <span>Facial</span><span class="uses__sep">·</span><span>Toner</span>
        <span>Scalp Scrub</span><span class="uses__sep">·</span><span>Hyperpigmentation</span>
      </p>
      <div class="powder-visual" role="img" aria-label="Photo of a heap of fine white glycolic acid powder"></div>
      <div class="free-from">
        <div class="free-from__value">0%</div>
        Fragrances<br>Additives<br>Dyes
      </div>
      <p class="net-weight">NET WT. 100G</p>
    </section>
  </main>
</body>
</html>
```